HarborLinen.net Trade Show banners

We need to do a design for 3 retractable banners that are 33" X 80" printed. The three banners will act as a back drop for our booth so there needs to be a left middle and a right, and fit together in a cohesive way. Our company is HarborLinen.net, we make custom mattresses and bedding for boats. we've attached a few pictures to be featured in the design. Please pick and choose at your discretion for your layout, you do not need to use them all, we just want to give you options. Our logo should be large, spanning across the three banners. I've also included the winning brochure design from a couple of years ago, along with a 10X10 banner that was made to go along with it.

What we liked about the design was that it included imagery of boating/sailing along with or pictures and images. Although the colors in the 10X10 banner were a bit too dark. We would like the colors to be brighter and more vibrant in the design and catch customers eyes, while not overshadowing the photos or our logo etc.

As for copy we would like the following. Under our logo it should say: Custom Boat Mattresses and Bedding

We would also like to see the following tag lines included in the design:
Let's make your stateroom a STATEMENT ROOM!
A Fresh Approach to Stateroom Design
Boat Bedding Made EASY
Patterns on file for over 1000 different boats.

Please feel free to ask any question. We will be very responsive throughout the project and look forward to seeing your designs.

-Marla & Dexter
HarborLinen.net

Target Market(s)

Men and women that own boats and yachts. Customers age range between Mid 30's to 80's

Industry/Entity Type

Marine

Font styles to use
Serif

Colors

Designer to choose colors to be used in the design.

Requirements
Must have
• The design should be very clean. While we included a lot of photos to choose from, less is more on a retractable banner. Pictures need to be visible from 10-12 feet away, as does text.
Nice to have
• It would be nice if the design shared some of the design elements of our website, but certainly it does not need nor should it be a copy of our home page.
Should not have
• The design should not be cluttered. It should not have text in the bottom 3rd of the banner.

```html
<!DOCTYPE html>
<html lang="en">
<head>
<meta charset="utf-8">
<title>HarborLinen.net Trade Show Banners</title>
<link href="https://fonts.googleapis.com/css2?family=Alegreya:ital,wght@0,400;0,500;1,400&display=swap" rel="stylesheet">
<style>
  :root {
    --backdrop: #a7afba;
    --navy: #1c2a55;
    --tag-blue: #2b4a8f;
    --brand-red: #c8252f;
    --frame: #f4f4f2;
    --sky-top: #c9d3e3;
    --sky-mid: #d9c7bd;
    --glow: #e0a776;
    --sea-mid: #8a6a58;
    --sea-deep: #4f3d3a;
    --footer-text: #ffffff;
  }
  * { box-sizing: border-box; margin: 0; padding: 0; }
  html, body {
    width: 1200px; height: 909px; overflow: hidden;
    background: var(--backdrop);
  }
  .booth {
    width: 1200px; height: 909px;
    display: flex; justify-content: center; align-items: center; gap: 50px;
  }
  .banner {
    position: relative;
    width: 330px; height: 800px;
    overflow: hidden;
    font-family: "Alegreya", Georgia, serif;
    color: var(--navy);
    display: flex; flex-direction: column; align-items: center;
    padding-bottom: 30px;
  }
  .banner__scene {
    position: absolute; inset: 0; z-index: 0;
    background:
      radial-gradient(ellipse 70% 25% at 60% 52%, rgba(240,180,120,.55), transparent 70%),
      linear-gradient(180deg, var(--sky-top) 0%, var(--sky-mid) 35%, var(--glow) 55%, var(--sea-mid) 72%, var(--sea-deep) 100%);
  }
  .brand, .tagline, .headline, .photos, .footer-line { position: relative; z-index: 1; }
  .brand {
    margin-top: 52px;
    display: flex; align-items: center; gap: 8px;
  }
  .brand__dot {
    width: 30px; height: 30px; border-radius: 50%;
    background: var(--brand-red);
  }
  .brand__name {
    font-size: 33px; font-weight: 500; color: var(--navy); letter-spacing: .2px;
  }
  .tagline {
    margin-top: 8px;
    font-style: italic; font-size: 15.5px; color: var(--tag-blue);
  }
  .headline {
    margin-top: 18px;
    text-align: center;
    font-size: 26px; font-weight: 500; line-height: 1.2;
  }
  .photos {
    margin-top: 20px;
    display: flex; flex-direction: column; gap: 8px;
  }
  .photo {
    width: 240px; height: 150px;
    border: 4px solid var(--frame);
  }
  .photo--oval-bed { background: linear-gradient(180deg, #6b3a24 0%, #b9a68c 45%, #8a7560 70%, #5a2a18 100%); }
  .photo--diamond-bed { background: linear-gradient(180deg, #e7ddd0 0%, #c9d4e3 25%, #d2706a 55%, #b84b48 100%); }
  .photo--navy-bed { background: linear-gradient(180deg, #e9e3da 0%, #d5a08c 30%, #2a2f5a 60%, #1d2248 100%); }
  .photo--cream-bed { background: linear-gradient(180deg, #7c4a34 0%, #d8cfc1 40%, #b8a690 70%, #5c2d1c 100%); }
  .photo--damask-bed { background: linear-gradient(180deg, #b36a48 0%, #d76d63 35%, #8fb7a8 65%, #c85a4e 100%); }
  .photo--anchor-bed { background: linear-gradient(180deg, #5a4236 0%, #d9d2cc 30%, #c4323a 45%, #1f2652 70%, #1a1f44 100%); }
  .photo--quilted-bed { background: linear-gradient(180deg, #4a4f58 0%, #e6e1da 40%, #b79a8a 70%, #8a4a34 100%); }
  .photo--mattress { background: linear-gradient(180deg, #5b5e62 0%, #dedcd8 40%, #c9c6c1 70%, #3a3b3e 100%); }
  .photo--teal-bed { background: linear-gradient(180deg, #c07a4e 0%, #d8503e 30%, #2f7a86 55%, #245f6a 100%); }
  .footer-line {
    margin-top: auto;
    text-align: center;
    font-style: italic; font-size: 14.5px; color: var(--footer-text);
    white-space: nowrap;
  }
</style>
</head>
<body>
<main class="booth">

  <section class="banner banner--left">
    <div class="banner__scene" role="img" aria-label="Sailing scene: pale sky over warm sunset light and rippling sea"></div>
    <div class="brand"><span class="brand__dot"></span><span class="brand__name">HarborLinen.net</span></div>
    <p class="tagline">Custom Boat Mattresses and Bedding</p>
    <h2 class="headline">Let's make your<br>Stateroom a<br>STATEMENT ROOM!</h2>
    <div class="photos">
      <div class="photo photo--oval-bed" role="img" aria-label="Photo of an oval stateroom bed with quilted beige cover"></div>
      <div class="photo photo--diamond-bed" role="img" aria-label="Photo of a bed with red and white diamond pattern bedspread"></div>
      <div class="photo photo--navy-bed" role="img" aria-label="Photo of a navy quilted bed with coral pillows"></div>
    </div>
    <p class="footer-line">Patterns on file for over 1000 different boats.</p>
  </section>

  <section class="banner banner--center">
    <div class="banner__scene" role="img" aria-label="Sailing scene: sky with clouds, sail and rigging over a glowing sea"></div>
    <div class="brand"><span class="brand__dot"></span><span class="brand__name">HarborLinen.net</span></div>
    <p class="tagline">Custom Boat Mattresses and Bedding</p>
    <h2 class="headline">Boat Bedding<br>Made EASY</h2>
    <div class="photos">
      <div class="photo photo--cream-bed" role="img" aria-label="Photo of a cream bed in a wood-panelled stateroom"></div>
      <div class="photo photo--damask-bed" role="img" aria-label="Photo of a bed with coral and aqua damask bedspread"></div>
      <div class="photo photo--anchor-bed" role="img" aria-label="Photo of a navy bed with anchor throw and red pillows"></div>
    </div>
    <p class="footer-line">Patterns on file for over 1000 different boats.</p>
  </section>

  <section class="banner banner--right">
    <div class="banner__scene" role="img" aria-label="Sailing scene: tall ship masts and rigging against a sunset over the sea"></div>
    <div class="brand"><span class="brand__dot"></span><span class="brand__name">HarborLinen.net</span></div>
    <p class="tagline">Custom Boat Mattresses and Bedding</p>
    <h2 class="headline">A Fresh Approach to<br>Stateroom Design</h2>
    <div class="photos">
      <div class="photo photo--quilted-bed" role="img" aria-label="Photo of a quilted bed with cream pillows"></div>
      <div class="photo photo--mattress" role="img" aria-label="Photo of a custom quilted boat mattress"></div>
      <div class="photo photo--teal-bed" role="img" aria-label="Photo of a teal bed with red and striped pillows"></div>
    </div>
    <p class="footer-line">Patterns on file for over 1000 different boats.</p>
  </section>

</main>
</body>
</html>
```